Brevik Fabrication - Business Card Design

We would like a dark (likely black) themed business card to be able to hand out to potential clients. We may list our services on the card or keep it clean. Unsure. Logo attached

```html
<!DOCTYPE html>
<html lang="en">
<head>
<meta charset="utf-8">
<title>Brevik Fabrication – Business Card</title>
<link rel="stylesheet" href="https://fonts.googleapis.com/css2?family=Open+Sans:wght@600;700&family=Crimson+Text&display=swap">
<style>
  :root{
    --page:#ffffff;
    --stage:#ebebeb;
    --card-grey:#646464;
    --card-dark:#1c1c1c;
    --band:#5e5e5e;
    --mark:#484848;
    --wordmark:#3a3a3a;
    --wordmark-back:#4e4e4e;
    --name:#1a1a1a;
    --muted:#7c7c7c;
    --tagline:#222222;
  }
  *{margin:0;padding:0;box-sizing:border-box}
  html,body{width:1200px;height:980px;overflow:hidden;background:var(--page)}
  .stage{position:absolute;left:16px;top:16px;width:1156px;height:937px;background:var(--stage)}
  .card{position:absolute;left:355px;width:514px;overflow:hidden}
  .card-shadow{position:absolute;background:#000;filter:blur(4px);opacity:.95}
  .front-shadow{left:334px;top:198px;width:514px;height:292px}
  .back-shadow{left:334px;top:568px;width:514px;height:292px}
  .front{top:168px;height:309px;background:var(--card-dark)}
  .front .upper{position:absolute;left:0;top:0;width:100%;height:166px;background:var(--card-grey)}
  .front .tagline-band{position:absolute;left:0;top:254px;width:100%;height:33px;background:var(--band)}
  .mark{position:absolute;border-radius:50%;background:var(--mark)}
  .front .mark{left:27px;top:86px;width:122px;height:122px}
  .wordmark{position:absolute;font-family:"Open Sans",sans-serif;font-weight:700;text-transform:uppercase;letter-spacing:.5px;white-space:nowrap}
  .front .wordmark{right:20px;top:20px;font-size:19px;color:var(--wordmark)}
  .person-name{position:absolute;left:212px;top:131px;font-family:"Open Sans",sans-serif;font-weight:700;font-size:38px;color:var(--name);line-height:1}
  .position{position:absolute;left:259px;top:169px;font-family:"Crimson Text",serif;font-size:18px;letter-spacing:6px;color:var(--muted);line-height:1}
  .contact{position:absolute;left:0;width:100%;font-family:"Crimson Text",serif;font-size:12.5px;color:var(--muted);line-height:1;letter-spacing:.4px}
  .contact-line{top:204px;padding-left:156px;word-spacing:1px}
  .contact-line .email{margin-left:12px}
  .web-line{top:224px;padding-left:223px}
  .tagline{position:absolute;left:168px;top:263px;font-family:"Crimson Text",serif;font-size:16px;color:var(--tagline);letter-spacing:.5px;line-height:1}
  .back{top:538px;height:309px;background:var(--card-dark)}
  .back .mark{left:185px;top:55px;width:144px;height:144px}
  .back .wordmark{left:0;width:100%;text-align:center;top:226px;font-size:21px;color:var(--wordmark-back)}
</style>
</head>
<body>
<div class="stage"></div>

<div class="card-shadow front-shadow"></div>
<section class="card front">
  <div class="upper"></div>
  <div class="tagline-band"></div>
  <div class="mark" role="img" aria-label="Brand mark"></div>
  <div class="wordmark">Brevik Fabrication</div>
  <h1 class="person-name">Your Name</h1>
  <p class="position">position</p>
  <p class="contact contact-line">Tel: +41 (0) 62 555 01 23 <span class="email">Email: company@brevikfab.com</span></p>
  <p class="contact web-line">www.your company website.com</p>
  <p class="tagline">Your Bussines Tagline</p>
</section>

<div class="card-shadow back-shadow"></div>
<section class="card back">
  <div class="mark" role="img" aria-label="Brand mark"></div>
  <div class="wordmark">Brevik Fabrication</div>
</section>
</body>
</html>
```